Wholesale e-commerce website re-design

We are a wholesaler of African-made and African-themed products, and we're looking to update the look and feel of our website www.terramarketgoods.com to improve user experience. We'd like to have a cleaner homepage that keeps the product category menus (but simplifies them), allows certain products to be featured, and has a simple CTA box (something like "Login" for existing wholesale customers or "Start a Business" for new customers). The layout might be something along the lines of http://www.pinewillowwares.com/ except with a shopping cart featured at the top right. Our colors tend to be earth-toned, but the current color palate looks dated. Also see our blog.terramarketgoods.com page for themes and color ideas that are maybe more up-to-date. On our product pages, we want to feature the products more prominently and have simpler, cleaner Buy or Add buttons.

Other reference sites for inspiration: vastherbalcrate.com, cozykitchenry.com, http://www.pinewillowwares.com, http://mbelatraders.com/ http://orunesa.com/

Reason: We like many of the designs that have been submitted so far, but need more time to make our final choice.

Target Market(s)

Small wholesale customers, most have a small business or home-based business. Also some retail, so an option for retail customers to click at the top to see retail pricing would be nice

Industry/Entity Type

Wholesale

Number of Pages Required

3 page

Font styles to use
Sans Serif

Requirements
Must have
• Clean, clear design that highlights products and reduces friction to customer purchase. Should include one homepage, one product page, and one shopping cart page design. Works with all browser types and be mobile-friendly.
Nice to have
• Other color schemes that would look good with our logo (maybe different from colors chosen below).
Should not have
• Splash pages with special effects, Adobe flash, elements that slow down page load times or that only work well in certain browsers.

```html
<!DOCTYPE html>
<html lang="en">
<head>
<meta charset="utf-8">
<title>Shopping Cart – Terra Market Goods</title>
<link href="https://fonts.googleapis.com/css2?family=Roboto:wght@400;500;700&family=Lato:wght@400;700&family=Fira+Sans:wght@500;600&display=swap" rel="stylesheet">
<style>
:root{
  --red:#c8372d;
  --red-soft:#fbd9d9;
  --dark:#5b5b5b;
  --darker:#4f4f4f;
  --ink:#222;
  --muted:#8a8a8a;
  --line:#dcdcdc;
  --band:#f3f3f3;
  --panel:#f0f0f0;
  --white:#fff;
}
*{box-sizing:border-box;margin:0;padding:0}
html,body{width:957px;height:1200px;overflow:hidden;background:var(--white)}
body{position:relative;font-family:"Roboto",sans-serif;color:var(--ink)}
.abs{position:absolute}
ul{list-style:none}

/* utility bar */
.util-bar{left:0;top:0;width:957px;height:27px;background:var(--dark)}
.util-bar .item{position:absolute;top:7px;font-size:11px;color:#eee;display:flex;align-items:center;gap:5px}
.util-bar .sep{position:absolute;top:6px;width:1px;height:16px;background:#777}

/* header */
.brand{left:80px;top:34px;width:80px;text-align:center;font-family:"Roboto",sans-serif;font-weight:700;font-size:15px;line-height:17px;color:var(--red);letter-spacing:1px}
.brand-mark{left:104px;top:72px;width:12px;height:12px;border-radius:50%;background:var(--red)}
.retail{left:262px;top:46px;font-family:"Fira Sans",sans-serif;font-size:10.5px;font-weight:500;line-height:12px}
.retail b{color:var(--red);font-weight:500;display:block;padding-left:18px}
.retail span{display:block;padding-left:18px}
.head-link{top:57px;font-family:"Fira Sans",sans-serif;font-weight:500;font-size:10.5px;display:flex;align-items:center;gap:6px}
.search{left:728px;top:55px;width:150px;height:23px;background:#eee;border-radius:2px}
.search-btn{left:854px;top:55px;width:24px;height:23px;background:var(--red);border-radius:2px;display:flex;align-items:center;justify-content:center}

/* nav */
.main-nav{left:0;top:98px;width:957px;height:36px;background:var(--red)}
.main-nav a{position:absolute;top:14px;font-family:"Fira Sans",sans-serif;font-weight:600;font-size:8.8px;color:#fff;text-decoration:none;letter-spacing:.2px}
.crumbs{left:0;top:134px;width:957px;height:33px;background:var(--band);border-bottom:1px solid #e6a6a0;font-family:"Fira Sans",sans-serif;font-size:8.5px}
.crumbs span{position:absolute;top:12px}

/* title */
.page-title{left:0;top:226px;width:957px;text-align:center;font-family:"Roboto",sans-serif;font-weight:700;font-size:28px;letter-spacing:.3px;color:#111}

/* cart table */
.checkout{left:589px;top:313px;width:289px;height:31px;background:var(--red);color:#fff;font-size:12px;font-weight:500;display:flex;align-items:center;justify-content:center;letter-spacing:.2px}
.cart-table{left:78px;top:352px;width:800px;height:128px;border:1px solid var(--line)}
.cart-head{position:absolute;left:0;top:0;width:798px;height:26px;background:var(--panel);border-bottom:1px solid var(--line)}
.cart-head span,.cell{position:absolute;font-size:10.5px}
.cart-head span{top:8px;font-weight:500}
.vline{position:absolute;top:0;width:1px;height:126px;background:var(--line)}
.thumb{left:10px;top:36px;width:82px;height:81px;border:1px solid var(--line);padding:6px}
.thumb div{width:100%;height:100%;background:linear-gradient(#e9e9e9,#cfcfcf)}
.qty{left:621px;top:416px;width:53px;height:24px;border:1px solid #ccc;font-size:11px;background:#fff}

.coupon-row{left:78px;top:480px;width:800px;height:48px;border-bottom:1px solid var(--line)}
.coupon-input{left:78px;top:491px;width:314px;height:27px;border:1px solid var(--line);background:#f7f7f7;font-size:11px;color:#555;padding:7px 8px}
.btn-gray{background:#e2e2e2;font-size:11.5px;font-weight:500;display:flex;align-items:center;justify-content:center;letter-spacing:.2px}
.totals{left:589px;top:528px;width:289px;height:149px;border:1px solid var(--line);border-top:none;background:#fff}
.totals .row{position:absolute;left:0;width:287px;border-top:1px solid var(--line);font-size:10.5px}
.calc{left:604px;top:592px;width:135px;height:30px;background:var(--red-soft);color:var(--red);font-size:12px;display:flex;align-items:center;justify-content:center}

/* features */
.features{left:0;top:720px;width:957px;height:116px;background:linear-gradient(#fff,#fafafa 50%,#fff);border-top:1px solid #f1f1f1;border-bottom:1px solid #f1f1f1}
.feat{position:absolute;width:180px;text-align:center}
.feat h3{font-family:"Lato",sans-serif;font-weight:400;font-size:13.5px;color:#111;margin-top:6px}
.feat p{font-family:"Lato",sans-serif;font-size:10px;color:var(--muted);margin-top:6px}

/* newsletter band */
.contact-band{left:0;top:873px;width:957px;height:58px;background:var(--dark)}
.email-input{left:78px;top:888px;width:197px;height:27px;background:#fff;font-family:"Lato",sans-serif;font-size:8.5px;color:#666;padding:9px 9px}
.subscribe{left:275px;top:888px;width:84px;height:27px;background:var(--red);color:#fff;font-family:"Lato",sans-serif;font-weight:700;font-size:11px;display:flex;align-items:center;justify-content:center}
.c-icon{width:24px;height:24px;border-radius:50%;background:var(--red);display:flex;align-items:center;justify-content:center}
.c-text{font-family:"Lato",sans-serif;color:#fff;font-size:9px;line-height:14px}
.c-text b{font-weight:700}

/* footer */
.footer{left:0;top:931px;width:957px;height:227px;background:#f2f2f2}
.f-col{position:absolute;top:26px}
.f-col h4{font-family:"Lato",sans-serif;font-weight:400;font-size:13.5px;color:#111;padding-bottom:7px;border-bottom:1px solid #ddd;position:relative}
.f-col h4::after{content:"";position:absolute;left:0;bottom:-1px;width:24px;height:1px;background:var(--red)}
.f-col li{font-family:"Lato",sans-serif;font-size:8.5px;color:#333;height:18.8px;line-height:18.8px;padding-left:14px;position:relative}
.f-col ul{margin-top:9px}
.f-col li::before{content:"";position:absolute;left:0;top:8px;width:4px;height:4px;border-radius:50%;background:#111}
.f-brand{left:370px;top:1000px;width:156px;text-align:center;font-family:"Roboto",sans-serif;font-weight:700;font-size:22px;line-height:26px;color:#cfcfcf;letter-spacing:1px}
.social{width:18px;height:18px;border-radius:50%;border:1px solid #9a9a9a;top:1116px}
.bottom-bar{left:0;top:1158px;width:957px;height:42px;background:var(--darker)}
.copy{left:80px;top:1171px;font-family:"Lato",sans-serif;font-size:11px;color:#eee}
.accept{left:682px;top:1146px;width:189px;height:42px;background:#fff;border:1px solid #bbb}
.accept .lbl{position:absolute;left:8px;top:-6px;background:#fff;padding:0 3px;font-family:"Lato",sans-serif;font-size:8px;color:#555}
.card{position:absolute;top:15px;width:28px;height:18px;border-radius:2px}
</style>
</head>
<body>

<!-- utility bar -->
<div class="abs util-bar">
  <div class="item" style="left:434px;top:6px">
    <svg width="14" height="12" viewBox="0 0 14 12"><path d="M7 0 0 6h2v6h4V8h2v4h4V6h2z" fill="#eee"/></svg>
  </div>
  <div class="item" style="left:470px"><svg width="12" height="11" viewBox="0 0 12 11"><rect x="0" y="3" width="12" height="3" fill="#eee"/><rect x="1" y="6" width="10" height="5" fill="#eee"/><rect x="5.3" y="3" width="1.4" height="8" fill="#5b5b5b"/></svg>Item Quick Order</div>
  <div class="sep" style="left:580px"></div>
  <div class="item" style="left:592px"><svg width="15" height="12" viewBox="0 0 15 12"><path d="M0 1h7l7 6-5 5-9-7z" fill="#eee"/><circle cx="3" cy="3.5" r="1.2" fill="#5b5b5b"/></svg>Get Promotions</div>
  <div class="sep" style="left:698px"></div>
  <div class="item" style="left:707px"><svg width="13" height="13" viewBox="0 0 13 13"><circle cx="6.5" cy="4" r="3.3" fill="#eee"/><path d="M0 13c0-4 3-6 6.5-6s6.5 2 6.5 6z" fill="#eee"/></svg>Your Account</div>
  <div class="sep" style="left:800px"></div>
  <div class="item" style="left:810px"><svg width="12" height="12" viewBox="0 0 12 12"><path d="M2 0l2.5 3-1.3 1.7c.8 1.7 2.2 3.1 3.9 3.9L8.8 7.3 12 9.8 10.2 12C4.8 11.5.5 7.2 0 1.8z" fill="#eee"/></svg>Contact Us</div>
</div>

<!-- header -->
<div class="abs brand">TERRA<br>MARKET</div>
<div class="abs brand-mark"></div>
<div class="abs retail">
  <svg class="abs" style="left:0;top:7px" width="15" height="13" viewBox="0 0 15 13"><path d="M0 1h7l7 6-5 5-9-7z" fill="#222"/><circle cx="3" cy="3.5" r="1.2" fill="#fff"/></svg>
  <b>Retail Pricing</b><span>For Retail Customers</span>
</div>
<div class="abs head-link" style="left:430px"><svg width="13" height="11" viewBox="0 0 13 11"><path d="M0 3.5h5V0l5 5.5-5 5.5V7.5H0z" fill="#222"/><rect x="11" y="0" width="2" height="11" fill="#222"/></svg>Sign In</div>
<div class="abs head-link" style="left:516px"><svg width="11" height="12" viewBox="0 0 11 12"><path d="M1 1h6v3M1 1v10h6" stroke="#222" stroke-width="1.4" fill="none"/><path d="M4 6h6M7 3l3 3-3 3" stroke="#222" stroke-width="1.4" fill="none"/></svg>Register</div>
<div class="abs head-link" style="left:598px">
  <svg width="18" height="14" viewBox="0 0 18 14"><path d="M0 1h3l2 8h9l2-6H4" stroke="#222" stroke-width="1.5" fill="none"/><circle cx="6" cy="12" r="1.4" fill="#222"/><circle cx="13" cy="12" r="1.4" fill="#222"/></svg>Shopping Cart
</div>
<div class="abs" style="left:614px;top:53px;width:9px;height:9px;border-radius:50%;background:var(--red);color:#fff;font-size:6px;text-align:center;line-height:9px">0</div>
<div class="abs search"></div>
<div class="abs search-btn"><svg width="13" height="13" viewBox="0 0 13 13"><circle cx="5.3" cy="5.3" r="4" stroke="#fff" stroke-width="1.7" fill="none"/><path d="M8.3 8.3 12 12" stroke="#fff" stroke-width="1.9"/></svg></div>

<!-- navigation -->
<nav class="abs main-nav">
  <a style="left:83px">African Clothing</a>
  <a style="left:167px">African Fabrics</a>
  <a style="left:251px">African Soaps</a>
  <a style="left:330px">Oils, Incense &amp; Burners</a>
  <a style="left:449px">Health &amp; Beauty</a>
  <a style="left:538px">New Items</a>
  <a style="left:602px">Jewelry</a>
  <a style="left:656px">Musical Instruments</a>
  <a style="left:761px">Artwork</a>
  <a style="left:815px">All Categories</a>
</nav>
<div class="abs crumbs">
  <span style="left:78px;color:#555">Home</span>
  <span style="left:112px;top:11px">⟶</span>
  <span style="left:136px;color:var(--red);font-weight:600">Shopping Cart</span>
</div>

<h1 class="abs page-title">SHOPPING CART</h1>

<!-- cart -->
<div class="abs checkout">PROCEED TO CHECKOUT</div>
<div class="abs cart-table">
  <div class="cart-head">
    <span style="left:11px">Product</span>
    <span style="left:448px">Price</span>
    <span style="left:545px">Quantity</span>
    <span style="left:661px">Total</span>
  </div>
  <div class="vline" style="left:413px"></div>
  <div class="vline" style="left:510px"></div>
  <div class="vline" style="left:627px"></div>
  <div class="vline" style="left:724px"></div>
  <div class="abs thumb"><div role="img" aria-label="Product photo: woman wearing a black turtle neck poncho"></div></div>
  <span class="cell" style="left:108px;top:61px">Turtle Neck Poncho</span>
  <span class="cell" style="left:444px;top:61px">$13.95.00</span>
  <span class="cell" style="left:654px;top:61px">$27.90</span>
  <svg class="abs" style="left:754px;top:56px" width="14" height="18" viewBox="0 0 14 18"><path d="M0 3h14M5 3V1h4v2" stroke="#c8372d" stroke-width="1.5" fill="none"/><rect x="1.8" y="4.5" width="10.4" height="12.7" rx="1" stroke="#c8372d" stroke-width="1.5" fill="none"/><path d="M5 7v8M7 7v8M9 7v8" stroke="#c8372d" stroke-width="1.1"/></svg>
</div>
<div class="abs qty"><span style="position:absolute;left:12px;top:5px">2</span><div style="position:absolute;left:30px;top:0;width:1px;height:22px;background:#ccc"></div><svg style="position:absolute;left:36px;top:4px" width="9" height="14" viewBox="0 0 9 14"><path d="M1 5 4.5 1 8 5zM1 9l3.5 4L8 9z" fill="#666"/></svg></div>

<div class="abs coupon-row"></div>
<div class="abs" style="left:589px;top:480px;width:289px;height:48px;background:var(--panel);border-left:1px solid var(--line);border-right:1px solid var(--line)"></div>
<div class="abs coupon-input">Coupon code</div>
<div class="abs btn-gray" style="left:434px;top:489px;width:127px;height:30px">APPLY COUPON</div>
<div class="abs btn-gray" style="left:728px;top:489px;width:136px;height:30px;color:var(--red)">UPDATE CART</div>

<div class="abs totals">
  <div class="row" style="top:0;height:34px"><span class="abs" style="left:15px;top:11px">Cart Subtotal</span><span class="abs" style="right:8px;top:11px;font-weight:500">$27.90</span></div>
  <div class="row" style="top:34px;height:80px"><span class="abs" style="left:15px;top:11px">Shipping and Handling</span><span class="abs" style="left:176px;top:10px;width:106px;text-align:right;font-size:10.2px;line-height:14.5px;color:#444">Please use the shipping calculator to see available s hipping methods.</span></div>
  <div class="row" style="top:114px;height:35px;background:var(--panel)"><span class="abs" style="left:15px;top:12px">Total</span><span class="abs" style="right:8px;top:12px;font-weight:500">$27.90</span></div>
  <div class="abs" style="left:164px;top:0;width:1px;height:149px;background:var(--line)"></div>
</div>
<div class="abs calc">Calculate Shipping</div>

<!-- features -->
<div class="abs features">
  <div class="feat" style="left:50px;top:26px">
    <svg width="34" height="26" viewBox="0 0 34 26"><circle cx="8" cy="20" r="4.5" stroke="#c8372d" stroke-width="2" fill="none"/><circle cx="27" cy="20" r="4.5" stroke="#c8372d" stroke-width="2" fill="none"/><path d="M12 18h11l2-7h-9zM14 11V4h8v7" fill="#c8372d"/><circle cx="18" cy="2.5" r="2.5" fill="#c8372d"/></svg>
    <h3>FREE DELIVERY</h3><p>24/7 Freeship</p>
  </div>
  <div class="feat" style="left:276px;top:26px">
    <svg width="34" height="22" viewBox="0 0 34 22"><path d="M2 8 26 1l6 10-24 10z" stroke="#c8372d" stroke-width="2" fill="none"/><text x="12" y="15" font-size="9" font-family="Roboto,sans-serif" font-weight="700" fill="#c8372d">%</text></svg>
    <h3>SALE &amp; DISCOUNT</h3><p>24/7 Freeship</p>
  </div>
  <div class="feat" style="left:512px;top:26px">
    <svg width="30" height="24" viewBox="0 0 30 24"><rect x="2" y="2" width="26" height="20" rx="2" stroke="#c8372d" stroke-width="2" fill="none"/><path d="M8 2v20M22 2v20M12 10h6l-1 4h-4z" stroke="#c8372d" stroke-width="1.6" fill="none"/></svg>
    <h3>EASY BUY ONLINE</h3><p>24/7 Freeship</p>
  </div>
  <div class="feat" style="left:736px;top:26px">
    <svg width="28" height="28" viewBox="0 0 28 28"><path d="M2 2h5l6 18h12" stroke="#c8372d" stroke-width="2" fill="none"/><rect x="11" y="4" width="11" height="7" transform="rotate(-18 16 8)" fill="#c8372d"/><rect x="13" y="11" width="11" height="7" transform="rotate(-18 18 14)" fill="#c8372d"/><circle cx="14" cy="24" r="2.5" fill="#c8372d"/></svg>
    <h3>WHOLESALER</h3><p>24/7 Freeship</p>
  </div>
</div>

<!-- contact band -->
<div class="abs contact-band"></div>
<div class="abs email-input">Enter your email here</div>
<div class="abs subscribe">Subscribe</div>
<div class="abs c-icon" style="left:394px;top:890px"><svg width="10" height="13" viewBox="0 0 10 13"><path d="M5 0a5 5 0 0 1 5 5c0 3.5-5 8-5 8S0 8.5 0 5a5 5 0 0 1 5-5z" fill="#fff"/><circle cx="5" cy="5" r="1.8" fill="#c8372d"/></svg></div>
<div class="abs c-text" style="left:427px;top:887px"><b>118 Cedar Mill Road, Suite B<br>Brookfield, OR 97402</b></div>
<div class="abs c-icon" style="left:595px;top:890px"><svg width="11" height="11" viewBox="0 0 12 12"><path d="M2 0l2.5 3-1.3 1.7c.8 1.7 2.2 3.1 3.9 3.9L8.8 7.3 12 9.8 10.2 12C4.8 11.5.5 7.2 0 1.8z" fill="#fff"/></svg></div>
<div class="abs c-text" style="left:628px;top:887px"><b>CALL US :</b><br><span style="font-size:11px">(503)555-0142</span></div>
<div class="abs c-icon" style="left:726px;top:890px"><svg width="11" height="8" viewBox="0 0 11 8"><rect width="11" height="8" fill="#fff"/><path d="M0 0l5.5 4.5L11 0" stroke="#c8372d" stroke-width="1.2" fill="none"/></svg></div>
<div class="abs c-text" style="left:760px;top:887px"><b>EMAIL US :</b><br>contact@terramarketgoods.com</div>

<!-- footer -->
<footer class="abs footer">
  <div class="f-col" style="left:78px;width:88px">
    <h4>QUICK LINKS</h4>
    <ul><li>Home</li><li>Item Quick Order</li><li>Web Specials</li><li>Top 10 Bestsellers</li><li>Your Account</li><li>Shopping Cart</li><li>About Us</li><li>Contact Us</li></ul>
  </div>
  <div class="f-col" style="left:214px;width:130px">
    <h4>BUSINESS TOOLS</h4>
    <ul><li>Free Printable Products</li><li>Get Your Own African Website</li><li>Fast Start-Up Kit</li><li>How to Start a New Business</li><li>Promotional Tools</li><li>Affiliate Program</li></ul>
  </div>
  <div class="f-col" style="left:547px;width:136px">
    <h4>CUSTOMER HELP</h4>
    <ul><li>Catalogs (New December Flier)</li><li>African Stores Near You</li><li>Frequently Asked Questions</li><li>Shipping Policies</li><li>See Retail Pricing</li></ul>
  </div>
  <div class="f-col" style="left:716px;width:162px">
    <h4>ABOUT TERRA MARKET</h4>
    <ul><li>About Terra Market Goods</li><li>How We Help Africa</li><li>African Proverbs</li><li>Free Articles</li><li>How Can We Improve?</li></ul>
  </div>
</footer>
<div class="abs f-brand">TERRA<br>MARKET</div>
<div class="abs social" style="left:393px"></div>
<div class="abs social" style="left:421px"></div>
<div class="abs social" style="left:451px"></div>
<div class="abs social" style="left:482px"></div>

<div class="abs bottom-bar"></div>
<div class="abs copy">Copyright © 2017 Terra Market Goods. All Right Reserved.</div>
<div class="abs accept">
  <span class="lbl">We Accept</span>
  <div class="card" style="left:8px;background:#e8eef7"></div>
  <div class="card" style="left:42px;background:#2a4f9a"></div>
  <div class="card" style="left:76px;background:#e9a23b"></div>
  <div class="card" style="left:110px;background:#f1f1f1;border:1px solid #ddd"></div>
  <div class="card" style="left:144px;background:#3a86c8"></div>
</div>

</body>
</html>
```